"Cork Hollow Excursions" is a top notch Santa Barbara County Wine Tour company.

We provide scenic, boutique and custom wine tours. I need the card to be clean and classy. I will provide our logo. I would like the logo to cover the back side of the card as an option and would like to see a couple color options other then our signature green and gold. I would like to see some creative options and let the designers come up with options.
I need cards for myself and my team. The final design should communicate "An authentic and boutique wine tour experience"
Please use my website for reference www.corkhollowexcursions.com

Target Market(s)

We have a wide range of clients from millennials to baby boomers

Industry/Entity Type

Tour

Contact Information for Business Card

Contact info:
Dale Munford
805-291-6384
info@corkhollowexcursions.com
corkhollowexcursions.com

Colors

Designer to choose colors to be used in the design.

Requirements
Must have
• my logo
Nice to have
• *I would like to have the backside side with the logo and the company statement
• "An authentic and boutique wine tour experience" as an option.
• *I would also like to see what the designers can create!
• *I would like to see an option that incorporates or social: snapgrid, rovia, route scout
Should not have
• I do not want it too busy.

```html
<!DOCTYPE html>
<html lang="en">
<head>
<meta charset="utf-8">
<title>Cork Hollow Excursions – Business Card</title>
<link rel="stylesheet" href="https://fonts.googleapis.com/css2?family=EB+Garamond:ital@1&family=Tinos:wght@400;700&display=swap">
<style>
  :root {
    --page: #ececec;
    --card: #ffffff;
    --green-dark: #164f14;
    --green-mid: #5d9160;
    --green-light: #a3c4a0;
    --gold: #c2b48a;
    --gold-strip: #bcb086;
    --ink: #111111;
    --wash: #e9f0e7;
  }
  * { margin: 0; padding: 0; box-sizing: border-box; }
  html, body {
    width: 981px; height: 1200px; overflow: hidden;
    background: var(--page);
  }
  .card {
    position: absolute; left: 109px;
    width: 763px; height: 437px;
    background: var(--card);
    overflow: hidden;
  }
  .card--front { top: 112px; }
  .card--back { top: 622px; }
  .card__shapes { position: absolute; inset: 0; }

  .brand {
    position: absolute; left: 200px; width: 466px; top: 0; height: 340px;
    text-align: center;
  }
  .brand__mark {
    position: absolute; left: 150px; top: 62px;
    width: 170px; height: 95px;
    background: linear-gradient(180deg, #dbe8d6 0%, #5d9160 55%, #1f6a1c 100%);
    border-radius: 4px;
  }
  .brand__name {
    position: absolute; left: 0; right: 0; top: 186px;
    font-family: "Tinos", serif; font-weight: 400;
    font-size: 30px; line-height: 36px; color: var(--green-dark);
  }
  .brand__tagline {
    position: absolute; left: 0; right: 0; top: 250px;
    font-family: "EB Garamond", serif; font-style: italic;
    font-size: 15px; line-height: 20px; color: var(--ink);
  }
  .social {
    position: absolute; left: 0; right: 0; top: 279px;
    display: flex; justify-content: center; gap: 12px;
    font-family: "Tinos", serif; font-size: 10px; line-height: 12px; color: var(--ink);
  }
  .social__item { display: flex; align-items: center; gap: 3px; }
  .social__dot { width: 9px; height: 9px; border-radius: 50%; background: var(--green-mid); }

  .watermark {
    position: absolute; left: 80px; top: 15px; width: 460px; height: 335px;
    background: radial-gradient(ellipse at 50% 55%, var(--wash) 0%, rgba(233,240,231,0.5) 50%, rgba(255,255,255,0) 75%);
  }
  .person {
    position: absolute; left: 55px; top: 52px;
    font-family: "Tinos", serif; font-weight: 700;
    font-size: 52px; line-height: 60px; color: var(--green-dark); letter-spacing: 0.5px;
  }
  .contacts { position: absolute; left: 61px; top: 136px; list-style: none; }
  .contacts__row {
    display: flex; align-items: center; gap: 20px;
    height: 29px; margin-bottom: 28px;
    font-family: "Tinos", serif; font-size: 24px; color: var(--ink);
  }
  .contacts__icon {
    width: 29px; height: 29px; border-radius: 50%;
    background: var(--gold);
    display: flex; align-items: center; justify-content: center;
    flex: none;
  }
</style>
</head>
<body>

<section class="card card--front" aria-label="Card front">
  <svg class="card__shapes" viewBox="0 0 763 437" width="763" height="437" aria-hidden="true">
    <path fill="var(--green-light)" d="M0,0 L82,0 C112,130 150,300 250,353 L0,353 Z"/>
    <path fill="var(--green-mid)" d="M0,0 L44,0 C72,150 120,295 225,353 L0,353 Z"/>
    <path fill="var(--green-dark)" d="M0,161 C70,245 120,320 205,353 L0,353 Z"/>
    <rect fill="var(--green-dark)" x="0" y="353" width="763" height="72"/>
    <rect fill="var(--gold-strip)" x="0" y="425" width="763" height="12"/>
  </svg>
  <div class="brand">
    <div class="brand__mark" role="img" aria-label="Company logo"></div>
    <div class="brand__name">Cork Hollow Excursions</div>
    <div class="brand__tagline">An authentic and boutique wine tour experience</div>
    <div class="social">
      <span class="social__item"><span class="social__dot"></span>snapgrid</span>
      <span class="social__item"><span class="social__dot"></span>route scout</span>
      <span class="social__item"><span class="social__dot"></span>rovia</span>
    </div>
  </div>
</section>

<section class="card card--back" aria-label="Card back">
  <div class="watermark" role="img" aria-label="Faint company logo decoration"></div>
  <svg class="card__shapes" viewBox="0 0 763 437" width="763" height="437" aria-hidden="true">
    <path fill="var(--green-light)" d="M763,0 L683,0 C655,130 620,300 530,352 L763,352 Z"/>
    <path fill="var(--green-mid)" d="M763,0 L727,0 C700,150 650,295 550,352 L763,352 Z"/>
    <path fill="var(--green-dark)" d="M763,163 C700,245 645,320 560,352 L763,352 Z"/>
    <rect fill="var(--green-dark)" x="0" y="352" width="763" height="73"/>
    <rect fill="var(--gold-strip)" x="0" y="425" width="763" height="12"/>
  </svg>
  <h1 class="person">DALE MUNFORD</h1>
  <ul class="contacts">
    <li class="contacts__row">
      <span class="contacts__icon">
        <svg width="13" height="13" viewBox="0 0 24 24" aria-hidden="true"><path fill="#fff" d="M6.6 10.8a15.1 15.1 0 0 0 6.6 6.6l2.2-2.2c.3-.3.7-.4 1-.2 1.1.4 2.3.6 3.6.6.6 0 1 .4 1 1V20c0 .6-.4 1-1 1C10.6 21 3 13.4 3 4c0-.6.4-1 1-1h3.5c.6 0 1 .4 1 1 0 1.3.2 2.5.6 3.6.1.3 0 .7-.2 1z"/></svg>
      </span>
      805-291-6384
    </li>
    <li class="contacts__row">
      <span class="contacts__icon">
        <svg width="13" height="13" viewBox="0 0 24 24" aria-hidden="true"><path fill="#fff" d="M3 5h18v14H3z"/><path fill="none" stroke="#c2b48a" stroke-width="1.8" d="M3 5l9 7 9-7"/></svg>
      </span>
      info@corkhollowexcursions.com
    </li>
    <li class="contacts__row">
      <span class="contacts__icon">
        <svg width="13" height="13" viewBox="0 0 24 24" aria-hidden="true"><circle cx="12" cy="12" r="9" fill="none" stroke="#fff" stroke-width="2"/><path fill="none" stroke="#fff" stroke-width="1.6" d="M3 12h18M12 3c3 3 3 15 0 18M12 3c-3 3-3 15 0 18"/></svg>
      </span>
      corkhollowexcursions.com
    </li>
  </ul>
</section>

</body>
</html>
```